Stationary and Business Card
Medical Practice
I need single sided standard sized Business Card [3.5" x 2"]
Letter type / font / color is up to the designer.
Professional
Benedict Harwell, MD
Torrance Ridge-Velmont Building
Suite 460
4127 Almaden Avenue
La Jolla, CA 92037
contact@brinmoor-example.com
www.drharwell-example.com
Please use provided logo.
Please visit drharwell-example.com for any additional creative direction.
Do not include email address.
Please provide a version with www.drharwell-example.com on the back of the card and a version with the web address on the front.

```html
<!DOCTYPE html>
<html lang="en">
<head>
<meta charset="utf-8">
<title>Harwell Stationery Set</title>
<link href="https://fonts.googleapis.com/css2?family=Cinzel:wght@500&family=Open+Sans:wght@400;600&display=swap" rel="stylesheet">
<style>
:root{
  --bg-dark:#6f7072;
  --bg-light:#a4a5a7;
  --paper:#ffffff;
  --blue-deep:#0d2f9e;
  --blue:#1f4fd1;
  --blue-light:#5f8cf2;
  --ink:#2a2a2a;
  --ink-soft:#6a6a6a;
  --rule:#c9c9c9;
}
*{margin:0;padding:0;box-sizing:border-box}
html,body{width:1200px;height:626px;overflow:hidden}
body{
  background:radial-gradient(ellipse at 55% 45%,var(--bg-light) 0%,var(--bg-dark) 85%);
  position:relative;font-family:"Open Sans",Arial,sans-serif;color:var(--ink);
}
.sheet{position:absolute;background:var(--paper);box-shadow:0 2px 6px rgba(0,0,0,.35);overflow:hidden}
.sheet svg.art{position:absolute;inset:0;width:100%;height:100%}
.brand{position:absolute;display:flex;flex-direction:column;align-items:flex-start}
.brand-row{display:flex;align-items:center;gap:5px}
.brand-mark{width:12px;height:12px;background:var(--blue)}
.brand-name{font-family:"Cinzel",Georgia,serif;font-weight:500;color:var(--ink);letter-spacing:1.5px}
.brand-tag{font-size:5px;letter-spacing:.8px;color:var(--ink-soft);margin-top:2px}
.small{font-size:5.5px;line-height:1.55;color:var(--ink-soft)}
.col{position:absolute}

.card-front{left:34px;top:197px;width:187px;height:101px;border-radius:6px}
.card-front .brand{left:0;right:0;top:30px;align-items:center}
.card-front .brand-name{font-size:15px}

.card-back{left:34px;top:312px;width:187px;height:101px;border-radius:6px}
.card-back .col{left:10px;top:12px;position:absolute}

.letterhead{left:233px;top:31px;width:429px;height:557px}
.letterhead .brand{left:24px;top:28px}
.letterhead .brand-name{font-size:13px}
.letterhead .foot-a{left:24px;bottom:20px}
.letterhead .foot-b{left:120px;bottom:20px}

.envelope-back{left:679px;top:79px;width:497px;height:238px}

.envelope-front{left:679px;top:334px;width:497px;height:235px}
.envelope-front .brand{left:40px;top:36px}
.envelope-front .brand-name{font-size:15px}
.envelope-front .foot-a{left:40px;bottom:18px}
.envelope-front .foot-b{left:140px;bottom:18px}
</style>
</head>
<body>

<section class="sheet card-front" aria-label="Business card front">
  <div class="brand">
    <div class="brand-row"><span class="brand-mark"></span><span class="brand-name">HARWELL</span></div>
    <div class="brand-tag">FAMILY MEDICAL PRACTICE</div>
  </div>
</section>

<section class="sheet card-back" aria-label="Business card back">
  <svg class="art" viewBox="0 0 187 101" preserveAspectRatio="none" aria-hidden="true">
    <defs>
      <linearGradient id="cardBlue" x1="0" y1="0" x2="1" y2="1">
        <stop offset="0" stop-color="var(--blue-light)"/>
        <stop offset=".5" stop-color="var(--blue)"/>
        <stop offset="1" stop-color="var(--blue-deep)"/>
      </linearGradient>
    </defs>
    <path d="M187 0 L120 0 C95 20,40 35,0 58 L0 101 L187 101 Z" fill="url(#cardBlue)"/>
    <path d="M120 0 C95 20,40 35,0 58" fill="none" stroke="#fff" stroke-width="1.4"/>
  </svg>
  <div class="col small">
    <div>www.drharwell-example.com</div>
    <div>Benedict Harwell, MD</div>
    <div>T 858 555 0142</div>
  </div>
</section>

<section class="sheet letterhead" aria-label="Letterhead">
  <svg class="art" viewBox="0 0 429 557" preserveAspectRatio="none" aria-hidden="true">
    <defs>
      <linearGradient id="lhBlue" x1="0" y1="0" x2="1" y2="0">
        <stop offset="0" stop-color="var(--blue-light)"/>
        <stop offset=".5" stop-color="var(--blue)"/>
        <stop offset="1" stop-color="var(--blue-deep)"/>
      </linearGradient>
    </defs>
    <path d="M429 0 L412 0 C385 130,400 260,388 380 C380 470,400 530,429 557 Z" fill="url(#lhBlue)"/>
    <path d="M404 0 C377 130,392 260,380 380 C372 470,392 530,420 557" fill="none" stroke="var(--rule)" stroke-width="1"/>
  </svg>
  <div class="brand">
    <div class="brand-row"><span class="brand-mark"></span><span class="brand-name">HARWELL</span></div>
    <div class="brand-tag">FAMILY MEDICAL PRACTICE</div>
  </div>
  <div class="col small foot-a">
    <div>Benedict Harwell, MD</div>
    <div>T 858 555 0142</div>
    <div>F 858 555 0143</div>
  </div>
  <div class="col small foot-b">
    <div>Torrance Ridge-Velmont Building</div>
    <div>Suite 460, 4127 Almaden Avenue</div>
    <div>La Jolla, CA 92037</div>
  </div>
</section>

<section class="sheet envelope-back" aria-label="Envelope back">
  <svg class="art" viewBox="0 0 497 238" preserveAspectRatio="none" aria-hidden="true">
    <defs>
      <radialGradient id="flapBlue" cx=".5" cy=".2" r=".7">
        <stop offset="0" stop-color="var(--blue-light)"/>
        <stop offset=".55" stop-color="var(--blue)"/>
        <stop offset="1" stop-color="var(--blue-deep)"/>
      </radialGradient>
    </defs>
    <path d="M0 0 L497 0 L497 95 L248 112 L0 95 Z" fill="url(#flapBlue)"/>
    <path d="M0 95 L248 112 L497 95" fill="none" stroke="var(--rule)" stroke-width="1"/>
  </svg>
</section>

<section class="sheet envelope-front" aria-label="Envelope front">
  <svg class="art" viewBox="0 0 497 235" preserveAspectRatio="none" aria-hidden="true">
    <defs>
      <linearGradient id="envBlue" x1="0" y1="0" x2="1" y2="0">
        <stop offset="0" stop-color="var(--blue-light)"/>
        <stop offset=".5" stop-color="var(--blue)"/>
        <stop offset="1" stop-color="var(--blue-deep)"/>
      </linearGradient>
    </defs>
    <path d="M497 0 L482 0 C460 70,478 150,455 235 L497 235 Z" fill="url(#envBlue)"/>
    <path d="M475 0 C453 70,471 150,448 235" fill="none" stroke="var(--rule)" stroke-width="1"/>
  </svg>
  <div class="brand">
    <div class="brand-row"><span class="brand-mark"></span><span class="brand-name">HARWELL</span></div>
    <div class="brand-tag">FAMILY MEDICAL PRACTICE</div>
  </div>
  <div class="col small foot-a">
    <div>Benedict Harwell, MD</div>
    <div>T 858 555 0142</div>
    <div>F 858 555 0143</div>
  </div>
  <div class="col small foot-b">
    <div>Torrance Ridge-Velmont Building</div>
    <div>Suite 460, 4127 Almaden Avenue</div>
    <div>La Jolla, CA 92037</div>
  </div>
</section>

</body>
</html>
```